Glow With Mirela, Enhancing Your Natural Bauty

Selling lipglosses, adding different types of photos with different colours of lip glosses,adding videos etc

Target Market(s)

All

Industry/Entity Type

Beauty industy

Coding

Coded - Design and coding required

Number of Pages Required

4 page

Requirements
Must have
• All payment options,easy to find,clear photos
Nice to have
• Photos of different ethnicity.Black,asian,white women

```html
<!DOCTYPE html>
<html lang="en">
<head>
<meta charset="utf-8">
<title>Glow With Mirela – Lip Gloss</title>
<link href="https://fonts.googleapis.com/css2?family=Inter:wght@400;500;600;700;800&display=swap" rel="stylesheet">
<style>
:root{
  --pink:#ea6592;
  --pink-2:#f07fa6;
  --pink-soft:#fbe3ea;
  --blush:#fdf2f5;
  --ink:#1b1b1f;
  --muted:#6b6b73;
  --line:#f1dde3;
  --star:#f5b400;
  --white:#fff;
}
*{box-sizing:border-box;margin:0;padding:0}
html,body{width:1200px;height:5179px;overflow:hidden}
body{font-family:"Inter",sans-serif;color:var(--ink);background:var(--white);position:relative}
.wrap{position:absolute;left:0;width:1200px}
svg{display:block}
.pink{color:var(--pink)}
.nav{top:0;height:66px;display:flex;align-items:center;padding:0 24px 0 20px;border-bottom:1px solid var(--line);background:#fff}
.brand{display:flex;align-items:center;gap:10px}
.brand-dot{width:34px;height:34px;border-radius:50%;background:var(--pink);flex:none}
.brand-name{font-weight:700;font-size:18px;color:var(--pink);line-height:1;white-space:nowrap}
.brand-tag{font-size:11px;color:var(--muted);margin-top:3px;white-space:nowrap}
.menu{display:flex;gap:30px;margin-left:30px;font-size:13px;font-weight:500;white-space:nowrap}
.search{margin-left:56px;width:350px;height:38px;border-radius:10px;background:#f6f6f7;display:flex;align-items:center;gap:10px;padding:0 14px;font-size:13px;color:#9a9aa2}
.nav-icons{margin-left:auto;display:flex;gap:30px;align-items:center}
.ico-badge{position:relative}
.ico-badge b{position:absolute;top:-12px;right:-10px;width:17px;height:17px;border-radius:50%;background:var(--pink);color:#fff;font-size:10px;display:flex;align-items:center;justify-content:center}
.hero{top:66px;height:664px;background:linear-gradient(180deg,#fff 0%,#fdf1f4 100%)}
.pill{position:absolute;left:16px;top:88px;height:38px;padding:0 18px;border-radius:20px;background:var(--pink-soft);color:var(--pink);font-size:13px;font-weight:500;display:flex;align-items:center;gap:8px}
.pill i{width:6px;height:6px;border-radius:50%;background:var(--pink)}
.hero h1{position:absolute;left:16px;top:140px;font-size:62px;line-height:64px;font-weight:800;letter-spacing:-1px}
.hero h1 span{color:var(--pink)}
.hero-rule{position:absolute;left:16px;top:274px;width:558px;height:2px;background:var(--pink-2);opacity:.6}
.hero p{position:absolute;left:16px;top:290px;width:470px;font-size:18px;line-height:30px;color:var(--muted)}
.btn-main{position:absolute;left:16px;top:380px;width:206px;height:44px;border-radius:10px;background:var(--pink);color:#fff;font-weight:600;font-size:14px;display:flex;align-items:center;justify-content:center;gap:14px}
.btn-ghost{position:absolute;left:244px;top:380px;width:196px;height:44px;border-radius:10px;background:#fff;border:1px solid var(--line);font-weight:500;font-size:14px;display:flex;align-items:center;justify-content:center;gap:14px}
.stats{position:absolute;left:16px;top:482px;display:flex;gap:36px}
.stat strong{display:block;font-size:24px;color:var(--pink);font-weight:700;text-align:center}
.stat span{font-size:13px;color:var(--muted)}
.hero-photo{position:absolute;left:622px;top:44px;width:556px;height:526px;border-radius:26px;
  background:radial-gradient(ellipse at 30% 35%,rgba(255,236,240,.75) 0%,rgba(255,236,240,0) 45%),
             linear-gradient(180deg,#f6c1cc 0%,#ee9fb2 55%,#e07f97 80%,#f3b8c6 100%)}
.float{position:absolute;background:#fff;border-radius:12px;box-shadow:0 8px 24px rgba(230,100,140,.2);display:flex;align-items:center;gap:10px;padding:0 12px;font-size:11px;white-space:nowrap}
.float i{width:34px;height:34px;border-radius:50%;background:var(--pink)}
.float b{display:block;font-weight:600}
.float span{color:var(--muted)}
.sec-title{position:absolute;left:0;width:1200px;text-align:center;font-size:38px;font-weight:800;letter-spacing:-.5px}
.sec-title span{color:var(--pink)}
.sec-desc{position:absolute;left:240px;width:720px;text-align:center;font-size:17px;line-height:30px;color:var(--muted)}
.collection{top:730px;height:1250px}
.deco-line{position:absolute;left:560px;top:54px;width:82px;height:4px;border-radius:2px;background:var(--pink)}
.tabs{position:absolute;left:20px;top:250px;width:1166px;height:64px;border-radius:10px;background:#f7f7f8;display:grid;grid-template-columns:repeat(7,1fr);padding:4px}
.tab{display:flex;flex-direction:column;align-items:center;justify-content:center;font-size:13px;font-weight:500;color:#555;border-radius:8px}
.tab small{font-size:11px;color:#999;margin-top:3px}
.tab.on{background:var(--pink);color:#fff}
.tab.on small{color:#fde}
.grid{position:absolute;left:20px;top:350px;width:1166px;display:grid;grid-template-columns:repeat(3,1fr);column-gap:24px;row-gap:34px}
.card{background:#fff;border-radius:14px;box-shadow:0 4px 18px rgba(0,0,0,.06);overflow:hidden;height:410px}
.ph{height:268px;position:relative}
.heart{position:absolute;right:14px;top:14px;width:36px;height:36px;border-radius:8px;background:#fff;display:flex;align-items:center;justify-content:center}
.tag{position:absolute;left:14px;height:20px;padding:0 10px;border-radius:5px;font-size:10px;font-weight:600;color:#fff;display:flex;align-items:center}
.sw{position:absolute;left:14px;bottom:12px;display:flex;gap:6px}
.sw i{width:22px;height:22px;border-radius:50%;border:2px solid #fff}
.cbody{padding:18px 18px}
.cname{font-size:18px;font-weight:600}
.rate{font-size:13px;color:var(--muted);margin-top:8px;display:flex;gap:6px;align-items:center}
.rate b{color:var(--ink);font-weight:600}
.star{color:var(--star)}
.crow{display:flex;align-items:center;justify-content:space-between;margin-top:16px}
.price{font-size:21px;font-weight:700;color:var(--pink)}
.price s{font-size:13px;color:#999;font-weight:400;margin-left:6px}
.add{width:136px;height:36px;border-radius:8px;background:var(--pink);color:#fff;font-size:13px;font-weight:600;display:flex;align-items:center;justify-content:center;gap:10px}
.learn{top:1980px;height:760px;background:#fdf3f6}
.vgrid{position:absolute;left:14px;top:230px;width:1164px;display:grid;grid-template-columns:repeat(3,1fr);gap:24px}
.vcard{background:#fff;border-radius:12px;overflow:hidden;height:396px;box-shadow:0 4px 16px rgba(0,0,0,.05)}
.vph{height:208px;position:relative}
.play{position:absolute;left:50%;top:50%;width:60px;height:60px;margin:-30px 0 0 -30px;border-radius:50%;background:var(--pink);display:flex;align-items:center;justify-content:center}
.dur{position:absolute;right:12px;bottom:12px;height:24px;padding:0 10px;border-radius:6px;background:rgba(0,0,0,.75);color:#fff;font-size:12px;display:flex;align-items:center;gap:6px}
.vbody{padding:18px 18px}
.vbody h3{font-size:17px;font-weight:600;line-height:24px}
.vbody p{font-size:13px;line-height:21px;color:var(--muted);margin-top:10px}
.vfoot{display:flex;justify-content:space-between;margin-top:18px;font-size:13px;color:var(--muted)}
.vfoot b{color:var(--ink);font-weight:600}
.btn-out{position:absolute;border:1px solid var(--line);background:#fff;border-radius:10px;font-size:13px;font-weight:600;display:flex;align-items:center;justify-content:center}
.reviews{top:2740px;height:1266px}
.summary{position:absolute;left:20px;top:276px;width:1166px;height:194px;border-radius:14px;background:#fcf6f8}
.big{position:absolute;left:34px;top:42px;font-size:48px;font-weight:700;color:var(--pink)}
.based{position:absolute;left:122px;top:52px;font-size:13px;color:var(--muted)}
.based .star{font-size:18px;display:block;margin-bottom:4px}
.bars{position:absolute;left:598px;top:30px;width:540px}
.bar{display:flex;align-items:center;height:30px;font-size:13px;color:var(--muted)}
.bar .n{width:32px}
.bar .track{width:404px;height:8px;border-radius:4px;background:#eee;margin:0 32px 0 0;overflow:hidden}
.bar .track i{display:block;height:100%;background:var(--pink);border-radius:4px}
.rgrid{position:absolute;left:20px;top:520px;width:1166px;display:grid;grid-template-columns:repeat(3,1fr);column-gap:24px;row-gap:16px}
.rcard{height:272px;border-radius:14px;background:#fff;box-shadow:0 4px 16px rgba(0,0,0,.05);padding:24px 26px;position:relative}
.rhead{display:flex;align-items:center;gap:10px}
.av{width:40px;height:40px;border-radius:50%;background:#ececec}
.rname{font-size:13px;font-weight:600;display:flex;gap:10px;align-items:center}
.ver{font-size:10px;font-weight:500;background:#f1e8ea;color:#7a5a63;padding:3px 10px;border-radius:10px}
.when{font-size:11px;color:var(--muted);margin-top:3px}
.quote{position:absolute;right:24px;top:24px;color:#f5b9cb;font-size:30px;font-weight:700;line-height:1}
.rstars{display:flex;align-items:center;gap:14px;margin-top:16px}
.rstars .star{font-size:17px;letter-spacing:2px}
.prod{font-size:10px;font-weight:500;background:#f5f0f1;padding:4px 10px;border-radius:10px}
.rtext{font-size:13px;line-height:24px;color:#55555d;margin-top:14px}
.rfoot{position:absolute;left:26px;right:26px;bottom:22px;display:flex;justify-content:space-between;font-size:11px;color:var(--muted)}
.rfoot span:last-child{color:var(--pink)}
.news{top:4006px;height:658px;background:linear-gradient(180deg,#fff 0%,#fdf4f6 100%)}
.nl-label{position:absolute;left:160px;top:74px;display:flex;gap:8px;align-items:center;font-size:13px;font-weight:500;color:var(--pink)}
.news h2{position:absolute;left:160px;top:108px;font-size:30px;font-weight:700}
.news h2 span{color:var(--pink)}
.news .lead{position:absolute;left:160px;top:164px;width:390px;font-size:15px;line-height:26px;color:var(--muted)}
.perk{position:absolute;left:160px;display:flex;gap:10px;align-items:center;font-size:13px}
.field{position:absolute;left:160px;top:294px;width:296px;height:40px;border:1px solid var(--line);border-radius:8px;background:#fff;font-size:13px;color:#888;display:flex;align-items:center;padding:0 14px}
.sub{position:absolute;left:466px;top:294px;width:100px;height:40px;border-radius:8px;background:var(--pink);color:#fff;font-size:13px;font-weight:600;display:flex;align-items:center;justify-content:center}
.fine{position:absolute;left:160px;top:360px;font-size:11px;color:var(--muted)}
.nl-photo{position:absolute;left:599px;top:0;width:472px;height:430px;
  background:radial-gradient(ellipse at 45% 40%,rgba(255,240,242,.85) 0%,rgba(255,240,242,0) 40%),
             linear-gradient(160deg,#f2c3ca 0%,#e99ea9 55%,#d48490 100%)}
.trust{position:absolute;left:0;width:1200px;top:476px;text-align:center;font-size:13px;color:var(--muted)}
.tstats{position:absolute;left:470px;top:512px;width:260px;display:flex;justify-content:space-between;text-align:center}
.tstats b{display:block;font-size:19px;color:var(--pink);font-weight:700}
.tstats span{font-size:11px;color:var(--muted)}
.footer{top:4664px;height:515px;background:#fdf3f6}
.fcol{position:absolute;top:100px}
.fcol h4{font-size:17px;font-weight:600;margin-bottom:22px}
.fcol li{list-style:none;font-size:13px;color:#555;margin-bottom:16px}
.fabout{font-size:13px;line-height:23px;color:#555;width:270px;margin-top:24px}
.socials{display:flex;gap:30px;margin-top:30px}
.socials i{width:18px;height:18px;border-radius:50%;border:1.5px solid #444}
.cline{display:flex;gap:14px;font-size:13px;color:#555;margin-bottom:18px;line-height:20px}
.fbar{position:absolute;left:20px;right:20px;top:450px;border-top:1px solid var(--line);padding-top:26px;display:flex;font-size:12px;color:#555}
.fbar .links{display:flex;gap:16px;margin-left:30px}
.fbar .made{margin-left:auto;display:flex;gap:8px;align-items:center}
</style>
</head>
<body>

<header class="wrap nav">
  <div class="brand">
    <div class="brand-dot"></div>
    <div><div class="brand-name">Glow With Mirela</div><div class="brand-tag">Enhancing Your Natural Beauty</div></div>
  </div>
  <nav class="menu"><span>New Arrivals</span><span>Best Sellers</span><span>Collections</span><span>About</span></nav>
  <div class="search"><svg width="15" height="15" viewBox="0 0 24 24" fill="none" stroke="#888" stroke-width="2"><circle cx="11" cy="11" r="7"/><path d="M20 20l-4-4"/></svg>Search for lip glosses...</div>
  <div class="nav-icons">
    <svg width="18" height="18" viewBox="0 0 24 24" fill="none" stroke="#222" stroke-width="2"><circle cx="12" cy="8" r="4"/><path d="M4 21c1-4 4-6 8-6s7 2 8 6"/></svg>
    <span class="ico-badge"><svg width="18" height="18" viewBox="0 0 24 24" fill="none" stroke="#222" stroke-width="2"><path d="M12 21s-8-5-8-11a4.5 4.5 0 0 1 8-2.5A4.5 4.5 0 0 1 20 10c0 6-8 11-8 11z"/></svg><b>5</b></span>
    <span class="ico-badge"><svg width="18" height="18" viewBox="0 0 24 24" fill="none" stroke="#222" stroke-width="2"><rect x="4" y="7" width="16" height="14" rx="2"/><path d="M9 7a3 3 0 0 1 6 0"/></svg><b>3</b></span>
  </div>
</header>

<section class="wrap hero">
  <div class="pill"><i></i>New Collection Available</div>
  <h1>Discover Your<br><span>Perfect Shade</span></h1>
  <div class="hero-rule"></div>
  <p>Premium lip glosses that enhance your natural beauty with long-lasting shine and vibrant colors.</p>
  <div class="btn-main">Shop Collection <svg width="14" height="14" viewBox="0 0 24 24" fill="none" stroke="#fff" stroke-width="2.5"><path d="M5 12h14M13 6l6 6-6 6"/></svg></div>
  <div class="btn-ghost"><svg width="12" height="12" viewBox="0 0 24 24" fill="none" stroke="#222" stroke-width="2.5"><path d="M6 4l14 8-14 8z"/></svg>Watch Tutorial</div>
  <div class="stats">
    <div class="stat"><strong>50+</strong><span>Shades Available</span></div>
    <div class="stat"><strong>10K+</strong><span>Happy Customers</span></div>
    <div class="stat"><strong>4.9★</strong><span>Average Rating</span></div>
  </div>
  <div class="hero-photo" role="img" aria-label="Product photo: row of pink lip gloss tubes and lipsticks standing on a pink backdrop"></div>
  <div class="float" style="left:618px;top:76px;height:58px"><i></i><div><b>Rose Quartz</b><span>$24.99</span></div></div>
  <div class="float" style="left:1040px;top:472px;height:58px"><i></i><div><b>Cherry Bomb</b><span>$26.99</span></div></div>
</section>

<section class="wrap collection">
  <div class="deco-line"></div>
  <h2 class="sec-title" style="top:72px">Our <span>Collection</span></h2>
  <p class="sec-desc" style="top:130px">Discover our curated selection of premium lip glosses, organized by color family to help you find your perfect match.</p>
  <div class="tabs">
    <div class="tab on">All Shades<small>(6)</small></div>
    <div class="tab">Pinks<small>(1)</small></div>
    <div class="tab">Nudes<small>(1)</small></div>
    <div class="tab">Reds<small>(1)</small></div>
    <div class="tab">Corals<small>(1)</small></div>
    <div class="tab">Berries<small>(1)</small></div>
    <div class="tab">Peaches<small>(1)</small></div>
  </div>
  <div class="grid">
    <article class="card">
      <div class="ph" role="img" aria-label="Product photo: close-up of glossy pink lips" style="background:radial-gradient(ellipse at 50% 55%,#e58b94 0%,#c96a72 45%,#d9a49c 100%)">
        <span class="tag" style="top:14px;background:var(--pink)">New</span>
        <span class="tag" style="top:40px;background:#e2324f">Save $5.00</span>
        <div class="heart"><svg width="16" height="16" viewBox="0 0 24 24" fill="none" stroke="#444" stroke-width="2"><path d="M12 21s-8-5-8-11a4.5 4.5 0 0 1 8-2.5A4.5 4.5 0 0 1 20 10c0 6-8 11-8 11z"/></svg></div>
        <div class="sw"><i style="background:#f6c5d2"></i><i style="background:#f4b3c2"></i><i style="background:#f8d3dc"></i></div>
      </div>
      <div class="cbody"><div class="cname pink">Rose Quartz Gloss</div><div class="rate"><span class="star">★</span><b>4.8</b>(124 reviews)</div>
      <div class="crow"><div class="price">$24.99<s>$29.99</s></div><div class="add"><svg width="13" height="13" viewBox="0 0 24 24" fill="none" stroke="#fff" stroke-width="2"><rect x="4" y="7" width="16" height="14" rx="2"/><path d="M9 7a3 3 0 0 1 6 0"/></svg>Add to Cart</div></div></div>
    </article>
    <article class="card">
      <div class="ph" role="img" aria-label="Product photo: row of nude lip gloss tubes" style="background:linear-gradient(90deg,#f4c9cf 0%,#eaa8b1 30%,#f6d9dd 55%,#e8a3ad 80%,#f7e3e6 100%)">
        <span class="tag" style="top:14px;background:var(--pink)">Best Seller</span>
        <div class="heart"><svg width="16" height="16" viewBox="0 0 24 24" fill="none" stroke="#444" stroke-width="2"><path d="M12 21s-8-5-8-11a4.5 4.5 0 0 1 8-2.5A4.5 4.5 0 0 1 20 10c0 6-8 11-8 11z"/></svg></div>
        <div class="sw"><i style="background:#d9b08c"></i><i style="background:#cfa57e"></i><i style="background:#e2c49d"></i></div>
      </div>
      <div class="cbody"><div class="cname">Nude Perfection</div><div class="rate"><span class="star">★</span><b>4.9</b>(89 reviews)</div>
      <div class="crow"><div class="price">$22.99</div><div class="add"><svg width="13" height="13" viewBox="0 0 24 24" fill="none" stroke="#fff" stroke-width="2"><rect x="4" y="7" width="16" height="14" rx="2"/><path d="M9 7a3 3 0 0 1 6 0"/></svg>Add to Cart</div></div></div>
    </article>
    <article class="card">
      <div class="ph" role="img" aria-label="Product photo: red lip gloss wand with a swatch on a pink surface" style="background:radial-gradient(ellipse at 45% 45%,#e9607a 0%,#f0a3b2 35%,#f6d2d9 100%)">
        <div class="heart"><svg width="16" height="16" viewBox="0 0 24 24" fill="none" stroke="#444" stroke-width="2"><path d="M12 21s-8-5-8-11a4.5 4.5 0 0 1 8-2.5A4.5 4.5 0 0 1 20 10c0 6-8 11-8 11z"/></svg></div>
        <div class="sw"><i style="background:#c8102e"></i><i style="background:#b00020"></i><i style="background:#9b1020"></i></div>
      </div>
      <div class="cbody"><div class="cname">Cherry Bomb</div><div class="rate"><span class="star">★</span><b>4.7</b>(156 reviews)</div>
      <div class="crow"><div class="price">$26.99</div><div class="add"><svg width="13" height="13" viewBox="0 0 24 24" fill="none" stroke="#fff" stroke-width="2"><rect x="4" y="7" width="16" height="14" rx="2"/><path d="M9 7a3 3 0 0 1 6 0"/></svg>Add to Cart</div></div></div>
    </article>
    <article class="card">
      <div class="ph" role="img" aria-label="Product photo: coral lip gloss tubes arranged on white" style="background:radial-gradient(ellipse at 60% 50%,#eba0a6 0%,#f3d4d2 45%,#f4f0ee 100%)">
        <div class="heart"><svg width="16" height="16" viewBox="0 0 24 24" fill="none" stroke="#444" stroke-width="2"><path d="M12 21s-8-5-8-11a4.5 4.5 0 0 1 8-2.5A4.5 4.5 0 0 1 20 10c0 6-8 11-8 11z"/></svg></div>
        <div class="sw"><i style="background:#f26b3a"></i><i style="background:#f47c5a"></i><i style="background:#f28a6c"></i></div>
      </div>
      <div class="cbody"><div class="cname">Coral Dreams</div><div class="rate"><span class="star">★</span><b>4.6</b>(78 reviews)</div>
      <div class="crow"><div class="price">$23.99</div><div class="add"><svg width="13" height="13" viewBox="0 0 24 24" fill="none" stroke="#fff" stroke-width="2"><rect x="4" y="7" width="16" height="14" rx="2"/><path d="M9 7a3 3 0 0 1 6 0"/></svg>Add to Cart</div></div></div>
    </article>
    <article class="card">
      <div class="ph" role="img" aria-label="Product photo: berry lip gloss on a lilac background" style="background:radial-gradient(ellipse at 50% 60%,#ee8fa8 0%,#dcaad9 40%,#c994cb 100%)">
        <div class="heart"><svg width="16" height="16" viewBox="0 0 24 24" fill="none" stroke="#444" stroke-width="2"><path d="M12 21s-8-5-8-11a4.5 4.5 0 0 1 8-2.5A4.5 4.5 0 0 1 20 10c0 6-8 11-8 11z"/></svg></div>
        <div class="sw"><i style="background:#7b1fa2"></i><i style="background:#9c27b0"></i><i style="background:#ab47bc"></i></div>
      </div>
      <div class="cbody"><div class="cname">Berry Bliss</div><div class="rate"><span class="star">★</span><b>4.8</b>(92 reviews)</div>
      <div class="crow"><div class="price">$25.99</div><div class="add"><svg width="13" height="13" viewBox="0 0 24 24" fill="none" stroke="#fff" stroke-width="2"><rect x="4" y="7" width="16" height="14" rx="2"/><path d="M9 7a3 3 0 0 1 6 0"/></svg>Add to Cart</div></div></div>
    </article>
    <article class="card">
      <div class="ph" role="img" aria-label="Product photo: close-up of glossy red lips" style="background:radial-gradient(ellipse at 50% 50%,#d6495c 0%,#b52f42 45%,#e2a497 100%)">
        <div class="heart"><svg width="16" height="16" viewBox="0 0 24 24" fill="none" stroke="#444" stroke-width="2"><path d="M12 21s-8-5-8-11a4.5 4.5 0 0 1 8-2.5A4.5 4.5 0 0 1 20 10c0 6-8 11-8 11z"/></svg></div>
        <div class="sw"><i style="background:#f7c9a0"></i><i style="background:#f5be8e"></i><i style="background:#f8d4b0"></i></div>
      </div>
      <div class="cbody"><div class="cname">Peachy Keen</div><div class="rate"><span class="star">★</span><b>4.5</b>(67 reviews)</div>
      <div class="crow"><div class="price">$21.99</div><div class="add"><svg width="13" height="13" viewBox="0 0 24 24" fill="none" stroke="#fff" stroke-width="2"><rect x="4" y="7" width="16" height="14" rx="2"/><path d="M9 7a3 3 0 0 1 6 0"/></svg>Add to Cart</div></div></div>
    </article>
  </div>
</section>

<section class="wrap learn">
  <h2 class="sec-title" style="top:52px">Learn &amp; <span>Get Inspired</span></h2>
  <p class="sec-desc" style="top:112px">Watch our tutorials and discover new ways to enhance your natural beauty with our lip gloss collection.</p>
  <div class="vgrid">
    <article class="vcard">
      <div class="vph" role="img" aria-label="Video still: applying lip liner and pink gloss" style="background:radial-gradient(ellipse at 45% 55%,#f07d95 0%,#d1506a 45%,#9b4b4a 100%)">
        <div class="play"><svg width="18" height="18" viewBox="0 0 24 24" fill="#fff"><path d="M7 4l13 8-13 8z"/></svg></div>
        <div class="dur"><svg width="11" height="11" viewBox="0 0 24 24" fill="none" stroke="#fff" stroke-width="2.5"><circle cx="12" cy="12" r="9"/><path d="M12 7v5l3 2"/></svg>3:54</div>
      </div>
      <div class="vbody"><h3 class="pink">HOW TO : ONLY LIP LINER AND GLOSS APPLICATION</h3><p>Learn the perfect technique for applying lip liner and gloss for a flawless finish.</p>
      <div class="vfoot"><span>◉ 12K views</span><b>Watch Now</b></div></div>
    </article>
    <article class="vcard">
      <div class="vph" role="img" aria-label="Video still: nude ombre lip look" style="background:linear-gradient(90deg,#c98a8c 0%,#b9777b 45%,#e1b3b2 55%,#c99294 100%)">
        <div class="play"><svg width="18" height="18" viewBox="0 0 24 24" fill="#fff"><path d="M7 4l13 8-13 8z"/></svg></div>
        <div class="dur"><svg width="11" height="11" viewBox="0 0 24 24" fill="none" stroke="#fff" stroke-width="2.5"><circle cx="12" cy="12" r="9"/><path d="M12 7v5l3 2"/></svg>10:58</div>
      </div>
      <div class="vbody"><h3>Ombre LipStick &amp; LipGloss Tutorial</h3><p>Step-by-step tutorial for creating beautiful ombre lip looks with our glosses.</p>
      <div class="vfoot"><span>◉ 8.5K views</span><b>Watch Now</b></div></div>
    </article>
    <article class="vcard">
      <div class="vph" role="img" aria-label="Video still: easy glossy lip routine with gloss tube" style="background:linear-gradient(90deg,#e58a56 0%,#c9673f 40%,#dcd9d2 60%,#c4cdc9 100%)">
        <div class="play"><svg width="18" height="18" viewBox="0 0 24 24" fill="#fff"><path d="M7 4l13 8-13 8z"/></svg></div>
        <div class="dur"><svg width="11" height="11" viewBox="0 0 24 24" fill="none" stroke="#fff" stroke-width="2.5"><circle cx="12" cy="12" r="9"/><path d="M12 7v5l3 2"/></svg>8:35</div>
      </div>
      <div class="vbody"><h3>GLOSSY LIP Makeup Tutorial</h3><p>Achieve the perfect glossy lip look with affordable makeup products.</p>
      <div class="vfoot"><span>◉ 15K views</span><b>Watch Now</b></div></div>
    </article>
  </div>
  <div class="btn-out" style="left:506px;top:678px;width:186px;height:40px">View All Tutorials</div>
</section>

<section class="wrap reviews">
  <h2 class="sec-title" style="top:104px"><span style="color:var(--star);font-size:22px;vertical-align:middle;margin-right:40px">☆</span>What Our <span>Customers Say</span><span style="color:var(--star);font-size:22px;vertical-align:top;margin-left:40px">☆</span></h2>
  <p class="sec-desc" style="top:164px">Don't just take our word for it - see what our satisfied customers have to say about our lip gloss collection.</p>
  <div class="summary">
    <div class="big">4.8</div>
    <div class="based"><span class="star">★★★★☆</span>Based on 1,247 reviews</div>
    <div class="bars">
      <div class="bar"><span class="n">5 <span class="star">★</span></span><span class="track"><i style="width:72%"></i></span>72%</div>
      <div class="bar"><span class="n">4 <span class="star">★</span></span><span class="track"><i style="width:20%"></i></span>20%</div>
      <div class="bar"><span class="n">3 <span class="star">★</span></span><span class="track"><i style="width:6%"></i></span>6%</div>
      <div class="bar"><span class="n">2 <span class="star">★</span></span><span class="track"><i style="width:1%"></i></span>1%</div>
      <div class="bar"><span class="n">1 <span class="star">★</span></span><span class="track"><i style="width:1%"></i></span>1%</div>
    </div>
  </div>
  <div class="rgrid">
    <article class="rcard"><div class="quote">❞</div><div class="rhead"><div class="av"></div><div><div class="rname">Lena Whitfield <span class="ver">Verified</span></div><div class="when">2 days ago</div></div></div>
      <div class="rstars"><span class="star">★★★★★</span><span class="prod">Rose Quartz Gloss</span></div>
      <p class="rtext">Absolutely love this lip gloss! The color is perfect for everyday wear and it lasts for hours without feeling sticky. The packaging is also gorgeous!</p>
      <div class="rfoot"><span>24 people found this helpful</span><span>Helpful</span></div></article>
    <article class="rcard"><div class="quote">❞</div><div class="rhead"><div class="av"></div><div><div class="rname">Nora Liang <span class="ver">Verified</span></div><div class="when">1 week ago</div></div></div>
      <div class="rstars"><span class="star">★★★★★</span><span class="prod">Nude Perfection</span></div>
      <p class="rtext">This is my holy grail nude lip gloss! It complements my skin tone perfectly and gives just the right amount of shine. Will definitely repurchase!</p>
      <div class="rfoot"><span>18 people found this helpful</span><span>Helpful</span></div></article>
    <article class="rcard"><div class="quote">❞</div><div class="rhead"><div class="av"></div><div><div class="rname">Carmen Ortega <span class="ver">Verified</span></div><div class="when">2 weeks ago</div></div></div>
      <div class="rstars"><span class="star">★★★★☆</span><span class="prod">Cherry Bomb</span></div>
      <p class="rtext">Beautiful bold color that makes a statement. The formula is smooth and comfortable to wear. Only wish it lasted a bit longer after eating.</p>
      <div class="rfoot"><span>12 people found this helpful</span><span>Helpful</span></div></article>
    <article class="rcard"><div class="quote">❞</div><div class="rhead"><div class="av"></div><div><div class="rname">Paige Morrow <span class="ver">Verified</span></div><div class="when">3 weeks ago</div></div></div>
      <div class="rstars"><span class="star">★★★★★</span><span class="prod">Coral Dreams</span></div>
      <p class="rtext">Perfect summer shade! The coral tone is so flattering and the gloss has the perfect consistency - not too thick, not too thin. Love it!</p>
      <div class="rfoot"><span>31 people found this helpful</span><span>Helpful</span></div></article>
    <article class="rcard"><div class="quote">❞</div><div class="rhead"><div class="av"></div><div><div class="rname">Dana Kessler <span class="ver">Verified</span></div><div class="when">1 month ago</div></div></div>
      <div class="rstars"><span class="star">★★★★★</span><span class="prod">Berry Bliss</span></div>
      <p class="rtext">This berry shade is stunning! It's become my go-to for date nights and special occasions. The quality is amazing for the price point.</p>
      <div class="rfoot"><span>15 people found this helpful</span><span>Helpful</span></div></article>
    <article class="rcard"><div class="quote">❞</div><div class="rhead"><div class="av"></div><div><div class="rname">Hana Seo <span class="ver">Verified</span></div><div class="when">1 month ago</div></div></div>
      <div class="rstars"><span class="star">★★★★☆</span><span class="prod">Peachy Keen</span></div>
      <p class="rtext">Such a pretty peachy pink! Perfect for spring and summer. The formula is hydrating and doesn't dry out my lips. Highly recommend!</p>
      <div class="rfoot"><span>9 people found this helpful</span><span>Helpful</span></div></article>
  </div>
  <div class="btn-out" style="left:422px;top:1122px;width:162px;height:52px;border:1.5px solid var(--pink);color:var(--pink);font-weight:500;font-size:14px">Write a Review</div>
  <div style="position:absolute;left:626px;top:1138px;font-size:14px;color:#555">View All Reviews</div>
</section>

<section class="wrap news">
  <div class="nl-label"><svg width="15" height="15" viewBox="0 0 24 24" fill="none" stroke="#ea6592" stroke-width="2"><rect x="3" y="5" width="18" height="14" rx="2"/><path d="M3 7l9 6 9-6"/></svg>Newsletter</div>
  <h2>Stay in the <span>Loop</span></h2>
  <p class="lead">Join our beauty community for exclusive offers and expert tips.</p>
  <div class="perk" style="top:230px"><svg width="14" height="14" viewBox="0 0 24 24" fill="none" stroke="#ea6592" stroke-width="2"><rect x="3" y="9" width="18" height="12" rx="1"/><path d="M12 9v12M3 13h18"/></svg>15% off your first order</div>
  <div class="perk" style="top:256px"><svg width="14" height="14" viewBox="0 0 24 24" fill="#ea6592"><path d="M12 2l2 7 7 3-7 3-2 7-2-7-7-3 7-3z"/></svg>Exclusive new launches</div>
  <div class="field">Enter your email</div>
  <div class="sub">Subscribe</div>
  <p class="fine">By subscribing, you agree to our Privacy Policy.</p>
  <div class="nl-photo" role="img" aria-label="Photo: makeup brushes with a cloud of pink powder above rose-gold lipsticks"></div>
  <p class="trust">Join over 25,000 beauty enthusiasts who trust Glow With Mirela</p>
  <div class="tstats"><div><b>25K+</b><span>Subscribers</span></div><div><b>4.9★</b><span>Rating</span></div><div><b>98%</b><span>Satisfaction</span></div></div>
</section>

<footer class="wrap footer">
  <div class="fcol" style="left:20px">
    <div class="brand"><div class="brand-dot"></div><div><div class="brand-name">Glow With Mirela</div><div class="brand-tag">Enhancing Your Natural Beauty</div></div></div>
    <p class="fabout">Premium lip glosses crafted with love to enhance your natural beauty. Discover your perfect shade and shine with confidence.</p>
    <div class="socials"><i></i><i></i><i></i><i></i></div>
  </div>
  <div class="fcol" style="left:320px"><h4>Quick Links</h4><ul><li>New Arrivals</li><li>Best Sellers</li><li>All Products</li><li>Gift Cards</li><li>Beauty Tips</li><li>Tutorials</li></ul></div>
  <div class="fcol" style="left:620px"><h4>Customer Care</h4><ul><li>Contact Us</li><li>Shipping Info</li><li>Returns &amp; Exchanges</li><li>Size Guide</li><li>FAQ</li><li>Track Your Order</li></ul></div>
  <div class="fcol" style="left:920px"><h4>Get in Touch</h4>
    <div class="cline"><svg width="16" height="16" viewBox="0 0 24 24" fill="none" stroke="#ea6592" stroke-width="2"><path d="M12 22s7-7 7-12a7 7 0 0 0-14 0c0 5 7 12 7 12z"/><circle cx="12" cy="10" r="2.5"/></svg><span>48 Blossom Lane<br>Pasadena, CA 91101</span></div>
    <div class="cline"><svg width="16" height="16" viewBox="0 0 24 24" fill="none" stroke="#ea6592" stroke-width="2"><path d="M5 3h4l2 5-3 2a12 12 0 0 0 6 6l2-3 5 2v4a2 2 0 0 1-2 2A17 17 0 0 1 3 5a2 2 0 0 1 2-2z"/></svg><span>+1 (555) 246-8100</span></div>
    <div class="cline"><svg width="16" height="16" viewBox="0 0 24 24" fill="none" stroke="#ea6592" stroke-width="2"><rect x="3" y="5" width="18" height="14" rx="2"/><path d="M3 7l9 6 9-6"/></svg><span>hello@glowwithmirela.com</span></div>
    <div style="font-size:13px;font-weight:600;margin-top:20px">Stay Updated</div>
    <div style="display:flex;gap:10px;margin-top:14px"><div style="width:214px;height:38px;border:1px solid var(--line);border-radius:8px;background:#fff;font-size:12px;color:#888;display:flex;align-items:center;padding:0 12px">Your email</div><div style="width:40px;height:38px;border-radius:8px;background:var(--pink);display:flex;align-items:center;justify-content:center"><svg width="15" height="15" viewBox="0 0 24 24" fill="none" stroke="#fff" stroke-width="2"><rect x="3" y="5" width="18" height="14" rx="2"/><path d="M3 7l9 6 9-6"/></svg></div></div>
  </div>
  <div class="fbar">© 2024 Glow With Mirela. All rights reserved.<div class="links"><span>Privacy Policy</span><span>Terms of Service</span><span>Cookie Policy</span></div>
    <div class="made">Made with <svg width="14" height="14" viewBox="0 0 24 24" fill="#ea6592"><path d="M12 21s-8-5-8-11a4.5 4.5 0 0 1 8-2.5A4.5 4.5 0 0 1 20 10c0 6-8 11-8 11z"/></svg> for beauty lovers</div></div>
</footer>

</body>
</html>
```